Letter head incorporating Our values and our Clover & Kite logo

here are our current letterheads, similar look and feel but incorporating our values logo too.
I have attached some of our flyers to give an idea of our look and feel of our brand

```html
<!DOCTYPE html>
<html lang="en">
<head>
<meta charset="utf-8">
<title>Clover &amp; Kite Letterhead</title>
<link href="https://fonts.googleapis.com/css2?family=Poppins:wght@400;500;700&display=swap" rel="stylesheet">
<style>
  :root {
    --backdrop: #e8e8e8;
    --paper: #ffffff;
    --sky: #00aeef;
    --orange: #f47b20;
    --green: #8dc63f;
    --green-deep: #39b54a;
    --red: #ed1c24;
    --yellow: #fff200;
    --wash-yellow: #fffbe3;
    --wash-blue: #e6f6fd;
  }
  * { margin: 0; padding: 0; box-sizing: border-box; }
  html, body { width: 1200px; height: 874px; overflow: hidden; }
  body {
    background: var(--backdrop);
    font-family: "Poppins", sans-serif;
    position: relative;
  }
  .letterhead {
    position: absolute;
    left: 310px;
    top: 27px;
    width: 580px;
    height: 820px;
    background: var(--paper);
    box-shadow: 0 4px 18px rgba(0,0,0,0.12);
    overflow: hidden;
  }
  .header-swoosh { position: absolute; left: 0; top: 0; width: 580px; height: 140px; }
  .brand {
    position: absolute;
    left: 30px;
    top: 112px;
    display: flex;
    align-items: center;
    gap: 8px;
  }
  .brand-dot { width: 16px; height: 16px; border-radius: 50%; background: var(--yellow); }
  .brand-name { font-weight: 700; font-size: 20px; color: var(--sky); line-height: 1; }
  .contact {
    position: absolute;
    right: 22px;
    top: 14px;
    color: #fff;
    font-style: normal;
    font-size: 8.5px;
    line-height: 1.35;
    text-align: right;
  }
  .contact-line { display: flex; justify-content: flex-end; align-items: center; gap: 5px; }
  .contact-line + .contact-line { margin-top: 1px; }
  .contact-address { margin-bottom: 4px; padding-right: 13px; }
  .contact-email { margin-top: 4px; }
  .contact-icon { width: 8px; height: 8px; flex: none; }
  .values-mark {
    position: absolute;
    left: 170px;
    top: 260px;
    width: 240px;
    height: 240px;
    border-radius: 24px;
    background: linear-gradient(160deg, var(--wash-yellow) 0%, var(--wash-yellow) 55%, var(--wash-blue) 100%);
  }
  .footer-band { position: absolute; left: 0; bottom: 0; width: 580px; height: 60px; }
  .footer-web {
    position: absolute;
    right: 22px;
    bottom: 14px;
    display: flex;
    align-items: center;
    gap: 6px;
    color: #fff;
    font-size: 11.5px;
    font-weight: 400;
    line-height: 1;
  }
  .footer-web svg { width: 10px; height: 10px; }
</style>
</head>
<body>
  <main class="letterhead">
    <svg class="header-swoosh" viewBox="0 0 580 140" aria-hidden="true">
      <path d="M0,0 H580 V108 C560,82 500,92 400,96 C230,100 80,48 0,74 Z" fill="var(--sky)"/>
      <path d="M0,80 C80,54 230,106 400,102 C500,99 560,90 580,116" fill="none" stroke="var(--orange)" stroke-width="3.5"/>
      <path d="M0,92 C70,62 230,112 400,108 C500,105 555,98 580,124" fill="none" stroke="var(--green)" stroke-width="3.5"/>
    </svg>

    <div class="brand">
      <span class="brand-dot"></span>
      <span class="brand-name">Clover &amp; Kite</span>
    </div>

    <address class="contact">
      <div class="contact-address">47 Wattle Grove Road<br>ASHBURY NSW 2193</div>
      <div class="contact-line">
        <span>(02) 5550 1482</span>
        <svg class="contact-icon" viewBox="0 0 10 10"><path d="M2,1 L4,1 L4.8,3.2 L3.6,4.2 C4.2,5.4 4.8,6 6,6.6 L7,5.4 L9,6.2 L9,8.2 C9,8.7 8.6,9 8,9 C4.5,8.6 1.4,5.5 1,2 C1,1.4 1.4,1 2,1 Z" fill="var(--yellow)"/></svg>
      </div>
      <div class="contact-line">
        <span>0400 555 218</span>
        <svg class="contact-icon" viewBox="0 0 10 10"><rect x="2.5" y="0.5" width="5" height="9" rx="1" fill="none" stroke="var(--green)" stroke-width="1"/><circle cx="5" cy="8" r="0.6" fill="var(--green)"/></svg>
      </div>
      <div class="contact-line contact-email">
        <span>ashbury@cloverandkite.edu.au</span>
        <svg class="contact-icon" viewBox="0 0 10 10"><rect x="0.5" y="2" width="9" height="6" rx="1" fill="var(--green)"/><path d="M0.8,2.4 L5,5.6 L9.2,2.4" fill="none" stroke="var(--sky)" stroke-width="0.8"/></svg>
      </div>
    </address>

    <div class="values-mark" role="img" aria-label="Placeholder for the faint Our Values mark"></div>

    <svg class="footer-band" viewBox="0 0 580 60" aria-hidden="true">
      <path d="M0,52 H355 C370,52 372,44 378,34 C386,22 394,20 410,20 H580 V60 H0 Z" fill="var(--sky)"/>
      <path d="M0,43 H58 L55,50 H0 Z" fill="var(--red)"/>
      <path d="M61,43 H140 L137,50 H58 Z" fill="var(--orange)"/>
      <path d="M143,43 H222 L219,50 H140 Z" fill="var(--green-deep)"/>
      <path d="M225,43 H302 L299,50 H222 Z" fill="var(--green)"/>
      <path d="M305,43 H345 C352,43 356,40 360,34 L362,31 L369,31 L366,36 C362,44 357,50 348,50 H302 Z" fill="var(--yellow)"/>
    </svg>
    <div class="footer-web">
      <svg viewBox="0 0 10 10" aria-hidden="true"><circle cx="5" cy="5" r="4.3" fill="none" stroke="#fff" stroke-width="0.9"/><ellipse cx="5" cy="5" rx="1.9" ry="4.3" fill="none" stroke="#fff" stroke-width="0.8"/><path d="M0.8,5 H9.2 M1.5,2.8 H8.5 M1.5,7.2 H8.5" stroke="#fff" stroke-width="0.7"/></svg>
      <span>www.cloverandkite.edu.au</span>
    </div>
  </main>
</body>
</html>
```